Website Design for Harrowgate & Pellinor LLC

We are looking for a new website design for our law firm. We have provided links to other websites that we find appealing.

```html
<!DOCTYPE html>
<html lang="en">
<head>
<meta charset="utf-8">
<title>Harrowgate &amp; Pellinor LLC — Website Design</title>
<link rel="stylesheet" href="https://fonts.googleapis.com/css2?family=Tinos:wght@400;700&family=Arimo:wght@400;700&display=swap">
<style>
:root{
  --olive:#4b5618;
  --olive-dark:#3d4712;
  --nav:#5e6d1e;
  --nav-light:#7a8a2c;
  --cream:#f3f8cf;
  --panel:#e8efb0;
  --panel-head:#e3eca6;
  --side:#1b220f;
  --side-head:#5b6a22;
  --side-text:#e8ecd4;
  --ink:#2a2a1a;
  --rule:#55622a;
}
*{margin:0;padding:0;box-sizing:border-box}
html,body{width:668px;height:1200px;overflow:hidden}
body{
  background:linear-gradient(#555 0%,#2c2c2c 46%,#5a5a5a 46.3%,#2a2a2a 100%);
  font-family:"Arimo",Arial,sans-serif;color:var(--ink);position:relative;
}
.page{position:absolute;left:52px;width:563px;background:var(--cream)}
.page--home{top:38px;height:474px}
.page--profile{top:555px;height:625px}
.masthead{position:absolute;left:0;top:0;width:563px;height:72px;background:var(--olive)}
.brand{position:absolute;left:14px;top:22px;color:#fff;font-family:"Tinos",serif;font-weight:400;font-size:17px;letter-spacing:.5px;white-space:nowrap}
.brand__suffix{position:absolute;left:176px;top:46px;color:#fff;font-family:"Tinos",serif;font-size:8px;letter-spacing:1px}
.masthead__photo{position:absolute;left:300px;top:0;width:263px;height:72px;background:linear-gradient(90deg,#4f5a2a 0%,#6f7d4a 30%,#8d9a88 55%,#6d7a52 80%,#4d6a2e 100%)}
.photo-strip{position:absolute;left:0;top:72px;width:563px;height:70px;background:linear-gradient(90deg,#8fa0a8 0%,#6f8a4a 18%,#3f6e2a 34%,#8a9fb5 52%,#5e7a8f 64%,#3f7a2a 78%,#5f8f2e 100%)}
.nav{position:absolute;left:0;top:142px;width:563px;height:22px;background:linear-gradient(var(--nav-light),var(--nav) 60%,var(--olive-dark));display:flex;align-items:center;font-family:"Tinos",serif;font-weight:700;font-size:8px;color:#fff;letter-spacing:.2px}
.nav__item{position:absolute;top:7px}
.nav__sep{position:absolute;top:5px;width:1px;height:11px;background:#fff}
.footer{position:absolute;left:0;bottom:0;width:563px;height:22px;background:var(--olive);color:#f0f0e0;font-family:"Tinos",serif;font-size:7px;text-align:center;line-height:22px}
.sidebar{position:absolute;left:421px;width:135px;background:var(--side);color:var(--side-text);font-family:"Tinos",serif}
.sidebar__head{background:var(--side-head);color:#fff;font-size:11px;padding:6px 0 6px 9px;letter-spacing:.2px}
.sidebar__head--center{text-align:center;padding-left:0}
.sidebar__list{list-style:none;padding:6px 9px 4px;font-size:8px;line-height:15.7px}
.sidebar__office{text-align:center;font-size:7.5px;padding:6px 0 2px}
.sidebar__phone{text-align:center;font-size:12px;color:#fff;letter-spacing:.2px}
.sidebar__address{padding:8px 9px 0;font-size:7.5px;line-height:15.5px;letter-spacing:.2px}
.sidebar__mail{text-align:center;font-size:6.5px;line-height:9px;padding:5px 0}
.clients{position:absolute;left:7px;top:179px;width:282px;height:267px;background:var(--panel);padding:11px 14px}
.clients__title{font-weight:700;font-size:8.5px;line-height:11px}
.clients__list{list-style:none;margin-top:8px;font-size:7.5px;line-height:16.5px}
.clients__services{list-style:none;margin-top:4px;font-size:7.3px;line-height:10px}
.clients__services li{position:relative;padding-left:8px;margin-bottom:4.7px}
.clients__services li::before{content:"*";position:absolute;left:0}
.project{position:absolute;left:305px;width:102px;text-align:center;font-family:"Tinos",serif;font-size:6px;line-height:8px;color:#333}
.project__photo{width:101px;height:63px;border:2px solid #fff;box-shadow:0 0 0 1px #999;margin-bottom:3px}
.portrait{position:absolute;left:7px;top:177px;width:113px;height:150px;background:#fff;border:1px solid #ccc;padding:4px}
.portrait__photo{width:100%;height:100%;background:linear-gradient(#b9c0c4,#9aa1a5 55%,#2a2a2e 75%,#1c1c20)}
.box-head{position:absolute;background:var(--panel-head);font-family:"Tinos",serif;font-size:10.5px;text-align:center}
.about__text{position:absolute;left:128px;top:214px;width:284px;font-size:7.5px;line-height:9.8px}
.about__text p+p{margin-top:9px}
.btn{position:absolute;left:128px;top:307px;width:72px;height:21px;background:var(--nav);color:#fff;font-family:"Tinos",serif;font-size:8.5px;text-align:center;line-height:21px;border:1px solid #3f4a12}
.divider{position:absolute;left:7px;top:340px;width:405px;height:2px;background:var(--rule)}
.col-list{position:absolute;list-style:none;font-size:7.3px;line-height:9px}
.col-list li{margin-bottom:6px}
</style>
</head>
<body>

<!-- Home page -->
<section class="page page--home">
  <header class="masthead">
    <div class="brand">HARROWGATE &amp; PELLINOR</div>
    <div class="brand__suffix">L.L.C.</div>
    <div class="masthead__photo" role="img" aria-label="Photo montage of a harbour statue and a stone manor house"></div>
  </header>
  <div class="photo-strip" role="img" aria-label="Photo banner: river marsh, town welcome sign, city skyline and lawn"></div>
  <nav class="nav">
    <span class="nav__item" style="left:25px">HOME</span><span class="nav__sep" style="left:66px"></span>
    <span class="nav__item" style="left:85px">ENVIRONMETAL LAW</span><span class="nav__sep" style="left:191px"></span>
    <span class="nav__item" style="left:210px">LAND USE / COMPLEX LITIGATION</span><span class="nav__sep" style="left:371px"></span>
    <span class="nav__item" style="left:390px">CORPORATE LAW / TRANSACTIONS</span>
  </nav>

  <div class="clients">
    <div class="clients__title">Harrowgate &amp; Pellinor, L.L.C.<br>Representative clients:</div>
    <ul class="clients__list">
      <li>Larkmoor Foils, Inc.</li>
      <li>Halvern Trust Bank</li>
      <li>Brightwater Hall Club</li>
      <li>Corvane Chemical Company, Inc.</li>
      <li>Thistle Realty</li>
      <li>Ashcombe Square Management, LLC</li>
      <li>Dunmere Chemical &amp; Mineral Corp.</li>
    </ul>
    <ul class="clients__services">
      <li>Transacting business in energy and high-tech industries;</li>
      <li>Owning or developing land;</li>
      <li>Structuring corporate entities;</li>
      <li>Engaging in site planning and redevelopment, including re-use of historic or contaminated parcels;</li>
      <li>Facing environmental enforcement actions or litigation;</li>
      <li>Litigating business disputes.</li>
    </ul>
  </div>

  <figure class="project" style="top:179px">
    <div class="project__photo" role="img" aria-label="Rendering of brick townhouse residences" style="background:linear-gradient(#c9d4de,#a8643f 45%,#7a4a32 80%,#5d6a3a)"></div>
    <figcaption>Client Project: The Residences<br>at Ashcombe Square, Wexley</figcaption>
  </figure>
  <figure class="project" style="top:271px">
    <div class="project__photo" role="img" aria-label="Rendering of a mixed residential tower" style="background:linear-gradient(#b8cde3,#c98a6a 40%,#a86a4a 75%,#6f8a3a)"></div>
    <figcaption>Client Project: Redevelopment<br>Institutional to Mixed Residential</figcaption>
  </figure>
  <figure class="project" style="top:363px">
    <div class="project__photo" role="img" aria-label="Photo of a historic colonnaded clubhouse in snow" style="background:linear-gradient(#d8dde2,#8a5a48 40%,#e8e8e8 70%,#f4f4f4)"></div>
    <figcaption>Client Project: Expansion of historic<br>Brightwater Hall Club</figcaption>
  </figure>

  <aside class="sidebar" style="top:179px;height:267px">
    <div class="sidebar__head">AREAS OF PRACTICE:</div>
    <ul class="sidebar__list">
      <li>Environmental Law</li><li>Land Use Law</li><li>Zoning</li><li>Redevelopment</li><li>Corporate Law</li><li>Complex Business</li><li>Litigation</li>
    </ul>
    <div class="sidebar__head sidebar__head--center" style="margin-top:4px">OFFICE LOCATIONS:</div>
    <div class="sidebar__office" style="padding-top:10px">WEXLEY, NJ</div>
    <div class="sidebar__phone">(555) 214 - 3800</div>
    <div class="sidebar__office" style="padding-top:14px">NEW YORK, NY</div>
    <div class="sidebar__phone">(555) 386 - 9207</div>
  </aside>

  <footer class="footer">Copyright © 2011 HARROWGATE &amp; PELLINOR All Rights Reserved.</footer>
</section>

<!-- Attorney profile page -->
<section class="page page--profile">
  <header class="masthead">
    <div class="brand">HARROWGATE &amp; PELLINOR</div>
    <div class="brand__suffix">L.L.C.</div>
    <div class="masthead__photo" role="img" aria-label="Photo montage of a harbour statue and a stone manor house"></div>
  </header>
  <div class="photo-strip" role="img" aria-label="Photo banner: river marsh, town welcome sign, city skyline and lawn"></div>
  <nav class="nav">
    <span class="nav__item" style="left:25px">HOME</span><span class="nav__sep" style="left:66px"></span>
    <span class="nav__item" style="left:85px">ENVIRONMETAL LAW</span><span class="nav__sep" style="left:191px"></span>
    <span class="nav__item" style="left:210px">LAND USE / COMPLEX LITIGATION</span><span class="nav__sep" style="left:371px"></span>
    <span class="nav__item" style="left:390px">CORPORATE LAW / TRANSACTIONS</span>
  </nav>

  <div class="portrait"><div class="portrait__photo" role="img" aria-label="Portrait photo of attorney Edwin R. Harrowgate"></div></div>
  <div class="box-head" style="left:128px;top:177px;width:284px;height:24px;line-height:24px">About Edwin R. Harrowgate</div>
  <div class="about__text">
    <p>Edwin R. Harrowgate has more than 30 years of experience at the highest levels of environmental law, counseling clients and representing them in litigation and administrative proceedings. Edwin's advice helps solve his clients' sophisticated business and regulatory issues in their business fields of energy, manufacturing, real estate and high tech.</p>
    <p>Edwin has represented his clients in a wide variety of matters, including state and federal enforcement actions in New York, New Jersey, and many other jurisdictions.</p>
  </div>
  <div class="btn">Read more</div>
  <div class="divider"></div>

  <div class="box-head" style="left:128px;top:352px;width:138px;height:25px;line-height:25px">Education</div>
  <div class="box-head" style="left:274px;top:352px;width:138px;height:25px;line-height:25px">Bar Associations</div>
  <ul class="col-list" style="left:127px;top:386px;width:140px">
    <li>Carrow School of Law, J.D., 1973</li>
    <li>University of Lindmere, B.A., 1970</li>
  </ul>
  <ul class="col-list" style="left:276px;top:386px;width:138px">
    <li>National Counsel Association</li>
    <li>Garden State Counsel Society</li>
    <li>Empire State Counsel Society</li>
    <li>Guild of Counsel of the City of New York</li>
  </ul>

  <div class="box-head" style="left:128px;top:459px;width:138px;height:25px;line-height:25px">Appointments:</div>
  <div class="box-head" style="left:274px;top:459px;width:138px;height:25px;line-height:25px">Bar Admissions</div>
  <ul class="col-list" style="left:127px;top:493px;width:140px">
    <li>Master of the Justice Warren T. Ellory</li>
    <li>Greenfield Inn of Court</li>
    <li>Former Associate of the NJ Chemical Industry Council</li>
    <li>Past Chair, Environmental Law Section</li>
    <li>Garden State Counsel Society</li>
  </ul>
  <ul class="col-list" style="left:276px;top:493px;width:138px">
    <li>National Counsel Association</li>
    <li>Garden State Counsel Society</li>
    <li>Empire State Counsel Society</li>
    <li>Guild of Counsel of the City of New York</li>
  </ul>

  <aside class="sidebar" style="top:177px;height:394px">
    <div class="sidebar__head">AREAS OF PRACTICE:</div>
    <ul class="sidebar__list">
      <li>CERCLA, Spill Act, Clean Air</li><li>Brownfields Redevelopment</li><li>Environmental Liability</li><li>Agency Enforcement Actions</li><li>Litigation</li><li>Complex Business Litigation</li><li>General Corporate Counsel</li>
    </ul>
    <div class="sidebar__head sidebar__head--center" style="margin-top:4px">CONTACT:</div>
    <div class="sidebar__address">HARROWGATE &amp; PELLINOR<br>L.L.C.<br>218 EAST 41ST STREET<br>SUITE# 902<br>NEW YORK, NY 10017</div>
    <div class="sidebar__office" style="padding-top:10px">PHONE</div>
    <div class="sidebar__phone">(555) 214 - 3800</div>
    <div class="sidebar__office" style="padding-top:4px">DIRECT</div>
    <div class="sidebar__phone">(555) 386 - 9207</div>
    <div class="sidebar__office" style="padding-top:4px">FAX</div>
    <div class="sidebar__phone">(555) 471 - 0629</div>
    <div class="sidebar__mail">edwin@harrowgatepellinor.example<br>eharrowgate@mail.example</div>
  </aside>

  <footer class="footer">Copyright © 2011 HARROWGATE &amp; PELLINOR All Rights Reserved.</footer>
</section>

</body>
</html>
```